Dental Business Card Design w/logo

Classic, elegant w/a touch of contemporary
Upscale dental facility located in Modesto CA
Specializing in restorative & general dentistry
Providing exceptional customer service to the community
Updates

I prefer script and not bold writing
If you can use the phone; fax and email icons instead of spelling them out, it would be great
No bold colors
Classy and elegant
In the back of the card I would like to see something like this
Your Next Appointment:
Mon     Tue    Wed    Thur (a box next to each of them for marking)
Date:_______________ at_____________ AM    PM  (a box next to them for marking)

Thank you

Target Market(s)

Well established professional

Industry/Entity Type

Dental

Contact Information for Business Card

Lavinteya Morbundi DMD
4176 Larkspur Rd
Suite F7
Modesto, CA 95355

Office: 209-731-5902
Fax: 209-731-8417
Email: morbundidmd@velmoranet.com

Requirements
Must have
• Unique classic logo
An easily repeatable design that can be used on letterhead and envelopes
Nice to have
• My initials incorporated into unique design
Should not have
• No cartoons or cheesy themes. This is a practice for the well established and professional individual.

```html
<!DOCTYPE html>
<html lang="en">
<head>
<meta charset="utf-8">
<title>Lavinteya Morbundi DMD – Business Card</title>
<link href="https://fonts.googleapis.com/css2?family=Source+Sans+3:wght@400&display=swap" rel="stylesheet">
<style>
  :root {
    --blue: #0b94d6;
    --white: #ffffff;
    --ink-grey: #7d7d7d;
    --label-grey: #666666;
    --card-edge: #2a2a2a;
    --stage-light: #f4f4f5;
    --stage-dark: #bfc0c2;
  }
  * { margin: 0; padding: 0; box-sizing: border-box; }
  html, body { width: 1200px; height: 1200px; overflow: hidden; }
  body {
    position: relative;
    font-family: "Source Sans 3", "Myriad Pro", Arial, sans-serif;
    background: radial-gradient(circle at 50% 48%, var(--stage-light) 0%, #e2e3e4 45%, var(--stage-dark) 100%);
    border: 2px solid #555;
  }
  .card {
    position: absolute;
    left: 229px;
    width: 742px;
    height: 422px;
    background: var(--white);
    border: 1px solid var(--card-edge);
    overflow: hidden;
  }
  .card--front { top: 170px; border-radius: 0 43px 0 43px; }
  .card--back { top: 607px; border-radius: 43px 0 43px 0; }
  .band { position: absolute; left: 0; width: 100%; background: var(--blue); }
  .card--front .band { top: 221px; height: 201px; }
  .card--back .band { top: 0; height: 199px; }

  .brand { position: absolute; display: flex; align-items: center; gap: 10px; font-size: 28px; line-height: 1; white-space: nowrap; }
  .brand__dot { width: 40px; height: 40px; border-radius: 50%; flex: none; }
  .card--front .brand { left: 350px; top: 78px; color: var(--ink-grey); }
  .card--front .brand__dot { background: var(--blue); }
  .card--back .brand { left: 58px; top: 63px; color: var(--white); }
  .card--back .brand__dot { background: var(--white); }

  .contact { position: absolute; left: 40px; top: 256px; list-style: none; color: var(--white); font-size: 18px; line-height: 20px; }
  .contact li { display: flex; align-items: flex-start; margin-bottom: 1px; }
  .contact li.contact__email { margin-top: 9px; }
  .contact svg { width: 22px; height: 22px; flex: none; margin-right: 10px; margin-top: -1px; }

  .appointment { position: absolute; left: 371px; top: 276px; color: var(--label-grey); font-size: 19px; line-height: 1; }
  .appointment__rows { margin: 11px 0 0 32px; }
  .appointment__row { display: flex; align-items: flex-end; margin-bottom: 9px; white-space: nowrap; }
  .tick-box { display: inline-block; width: 15px; height: 15px; border: 1.4px solid var(--label-grey); margin: 0 4px 2px 2px; }
  .blank { display: inline-block; border-bottom: 1.4px solid var(--label-grey); margin-bottom: 2px; }
  .blank--date { width: 82px; }
  .blank--time { width: 50px; }
</style>
</head>
<body>

<section class="card card--front" aria-label="Card front">
  <div class="brand"><span class="brand__dot"></span><span class="brand__name">Lavinteya Morbundi DMD</span></div>
  <div class="band"></div>
  <ul class="contact">
    <li>
      <svg viewBox="0 0 22 22" aria-hidden="true"><circle cx="11" cy="11" r="11" fill="#fff"/><path d="M5 11.5 11 6l6 5.5h-2V16H7v-4.5z" fill="var(--blue)"/><rect x="10" y="12.5" width="2" height="3.5" fill="#fff"/></svg>
      <span>4176 Larkspur Rd Suite F7 Modesto,<br>CA 95355</span>
    </li>
    <li>
      <svg viewBox="0 0 22 22" aria-hidden="true"><circle cx="11" cy="11" r="11" fill="#fff"/><path d="M7 5.5c1-.6 1.8-.3 2.3.5l1 1.8c.3.7 0 1.3-.6 1.6l-.8.4c.6 1.6 1.6 2.7 3.2 3.4l.5-.8c.4-.6 1-.8 1.6-.5l1.8 1c.8.5 1 1.3.4 2.2-.8 1.3-2.2 1.6-3.6 1-3.2-1.3-5.6-3.8-6.7-7-.5-1.5 0-2.8.9-3.6z" fill="var(--blue)"/></svg>
      <span>209-731-5902</span>
    </li>
    <li>
      <svg viewBox="0 0 22 22" aria-hidden="true"><circle cx="11" cy="11" r="11" fill="#fff"/><rect x="7.5" y="4.5" width="7" height="4" fill="var(--blue)"/><rect x="5" y="9" width="12" height="6" rx="1" fill="var(--blue)"/><rect x="7.5" y="13" width="7" height="4.5" fill="var(--blue)" stroke="#fff" stroke-width="1"/></svg>
      <span>209-731-8417</span>
    </li>
    <li class="contact__email">
      <svg viewBox="0 0 22 22" aria-hidden="true"><circle cx="11" cy="11" r="11" fill="#fff"/><rect x="5" y="7" width="12" height="8.5" fill="var(--blue)"/><path d="M5 7l6 5 6-5" fill="none" stroke="#fff" stroke-width="1.2"/></svg>
      <span>morbundidmd@velmoranet.com</span>
    </li>
  </ul>
</section>

<section class="card card--back" aria-label="Card back">
  <div class="band"></div>
  <div class="brand"><span class="brand__dot"></span><span class="brand__name">Lavinteya Morbundi DMD</span></div>
  <div class="appointment">
    <p class="appointment__title">Next Appointment:</p>
    <div class="appointment__rows">
      <p class="appointment__row">Mon<span class="tick-box"></span>Tue<span class="tick-box"></span>Wed<span class="tick-box"></span>Thur<span class="tick-box"></span></p>
      <p class="appointment__row">Date:<span class="blank blank--date"></span>at<span class="blank blank--time"></span>AM<span class="tick-box"></span>&nbsp;PM<span class="tick-box"></span></p>
    </div>
  </div>
</section>

</body>
</html>
```